International service dog training school needs web design

We need to upgrade our website. The website is https://brevantmoor.example/
We help trainers and service dog programs learn how to train service dogs with the latest and most ethical training methods. We offer online and in-person coaching services. We would like to see designs that are engaging and communicate professionalism, expertise, and care for the dogs and people we work with. Please also keep the colors already in the logo in the design.

```html
<!DOCTYPE html>
<html lang="en">
<head>
<meta charset="utf-8">
<title>Brevant Moor Institute – Alert Dog Coaching</title>
<link href="https://fonts.googleapis.com/css2?family=Oswald:wght@400;500;600&family=Roboto:wght@300;400;500;700&display=swap" rel="stylesheet">
<style>
:root{
  --teal:#17a398;
  --blue:#2b7fcf;
  --ink:#222;
  --grey:#666;
  --dark:#161616;
  --darker:#0e0e0e;
  --band:#e9f1f6;
  --footer:#1c1c1c;
  --gold1:#c99a52;
  --gold2:#7a5a30;
  --white:#fff;
}
*{box-sizing:border-box;margin:0;padding:0}
html,body{width:1200px;height:3728px;overflow:hidden}
body{font-family:"Roboto",sans-serif;color:var(--ink);background:var(--white);position:relative}
.abs{position:absolute}
.btn{display:inline-block;background:var(--teal);color:#fff;font:500 10px "Roboto",sans-serif;letter-spacing:.08em;text-transform:uppercase;padding:8px 16px;border-radius:2px}
.btn.dark{background:var(--dark)}
.photo{border-radius:2px}

/* header */
.site-header{left:0;top:0;width:1200px;height:88px;background:var(--darker)}
.brand{left:40px;top:14px;display:flex;align-items:center;gap:10px;color:#fff;font:500 15px "Roboto",sans-serif;letter-spacing:.02em}
.brand-mark{width:28px;height:28px;border-radius:50%;background:var(--teal)}
.brand small{display:block;font:300 10px "Roboto",sans-serif;color:#bbb;letter-spacing:.06em}
.socials{right:40px;top:14px;display:flex;gap:8px}
.socials span{width:22px;height:22px;border-radius:50%}
.s1{background:#3b5a9a}.s2{background:#2aa4e0}.s3{background:#d8312a}
.header-mail{right:140px;top:18px;color:#ccc;font-size:11px}
.main-nav{left:40px;top:58px;display:flex;gap:4px}
.main-nav a{color:#ddd;font:500 11px "Roboto",sans-serif;text-transform:uppercase;letter-spacing:.08em;padding:8px 14px;text-decoration:none}
.main-nav a.active{background:var(--teal);color:#fff}

/* hero */
.hero{left:0;top:88px;width:1200px;height:824px;background:var(--dark)}
.hero-photo{left:40px;top:0;width:800px;height:440px;background:linear-gradient(110deg,#3d4f3a 0%,var(--gold1) 45%,var(--gold2) 75%,var(--dark) 100%)}
.hero-copy{left:672px;top:140px;color:#fff}
.hero-copy .kicker{font:400 22px "Oswald",sans-serif;letter-spacing:.02em}
.hero-copy h1{font:600 38px/1.05 "Oswald",sans-serif;text-transform:uppercase;margin-top:4px}
.hero-copy .btn{margin-top:18px}

.center-card{left:144px;top:452px;width:456px;height:372px;background:var(--blue);color:#fff;padding:34px 32px}
.center-card .pre{font:500 13px "Roboto",sans-serif;text-transform:uppercase;letter-spacing:.04em}
.center-card h2{font:400 30px/1.15 "Roboto",sans-serif;margin-top:6px}
.center-card p{font:300 12px/1.6 "Roboto",sans-serif;margin-top:16px;opacity:.95}
.center-card .btn{margin-top:18px;background:#fff;color:var(--blue)}
.founder-card{left:600px;top:452px;width:460px;height:372px;background:#fff;padding:34px 32px;text-align:center}
.founder-card h3{text-align:left;font:500 13px "Roboto",sans-serif;letter-spacing:.06em;text-transform:uppercase}
.avatar{width:56px;height:56px;border-radius:50%;margin:20px auto 0;background:linear-gradient(135deg,#b88a6a,#5b3c2c)}
.founder-card blockquote{font:italic 300 12px/1.6 "Roboto",sans-serif;color:var(--grey);margin-top:18px;padding:0 20px}
.founder-card .sig{font:500 13px "Roboto",sans-serif;margin-top:14px}
.founder-card .role{font-size:11px;color:var(--grey)}

/* courses */
.courses-title{left:0;top:964px;width:1200px;text-align:center;font:500 30px "Roboto",sans-serif}
.course{width:308px}
.course .photo{width:308px;height:180px;background:linear-gradient(135deg,#9aa6ad,#5d6b73)}
.course h4{font:500 13px "Roboto",sans-serif;margin-top:12px}
.course p{font:300 11px/1.6 "Roboto",sans-serif;color:var(--grey);margin-top:6px;height:72px}
.course .btn{margin-top:10px}

/* assistance canines */
.band{left:0;top:1952px;width:1200px;height:588px;background:var(--band)}
.dog-art{left:520px;top:1720px;width:160px;height:280px;border-radius:80px 80px 20px 20px;background:radial-gradient(circle at 50% 35%,#e0b46e,#b27c3c 70%,#8a5a28)}
.big-word{top:1968px;font:400 70px/1 "Oswald",sans-serif;color:#7b8085;letter-spacing:.02em}
.arrow{top:2190px;width:30px;height:30px}
.slide{width:290px}
.slide .photo{width:290px;height:176px;background:linear-gradient(135deg,#a7b3a0,#5f6e5c)}
.slide h4{font:500 13px "Roboto",sans-serif;margin-top:12px}
.slide p{font:300 11px/1.6 "Roboto",sans-serif;color:var(--grey);margin-top:6px}
.slide .btn{margin-top:12px}

/* book */
.book{left:160px;top:2590px;width:300px;height:380px;background:linear-gradient(150deg,#f4efe4,#d8c9a8 60%,#b6453a);transform:rotate(-6deg);box-shadow:0 10px 20px rgba(0,0,0,.2)}
.book-copy{left:680px;top:2660px;width:480px;text-align:center}
.book-copy .pre{font:500 12px "Roboto",sans-serif;letter-spacing:.08em;text-transform:uppercase}
.book-copy h2{font:500 34px "Oswald",sans-serif;margin-top:4px}
.book-copy p{font:300 11px "Roboto",sans-serif;color:var(--grey);margin-top:8px}
.book-copy .btn{margin-top:18px}

/* staying ahead */
.ahead{left:0;top:2932px;width:1200px;height:228px;background:linear-gradient(180deg,#2f4862,#17263a);text-align:center;color:#fff;padding-top:76px}
.ahead h2{font:500 28px "Oswald",sans-serif;letter-spacing:.06em;text-transform:uppercase}
.ahead p{font:300 12px "Roboto",sans-serif;margin-top:6px;color:#d6dee8}
.ahead .btn{margin-top:14px}

/* footer */
.site-footer{left:0;top:3220px;width:1200px;height:508px;background:var(--footer);color:#bbb}
.fcol{top:60px;font-size:11px;line-height:2}
.fcol h5{color:#fff;font:500 12px "Roboto",sans-serif;text-transform:uppercase;letter-spacing:.06em;margin-bottom:10px}
.fcol .ico{display:inline-block;width:10px;height:10px;border-radius:50%;background:var(--teal);margin-right:8px;vertical-align:middle}
.field{width:140px;height:24px;background:#2c2c2c;margin-bottom:8px}
.fsoc{display:flex;align-items:center;gap:8px}
.fsoc span{width:18px;height:18px;border-radius:50%}
.copyright{left:0;top:450px;width:1200px;text-align:center;font-size:10px;color:#888;border-top:1px solid #2e2e2e;padding-top:16px}
</style>
</head>
<body>

<header class="site-header abs">
  <div class="brand abs"><span class="brand-mark"></span><div>Brevant Moor Institute<small>ALERT DOG COACHING</small></div></div>
  <div class="header-mail abs">hello@brevantmoor.example</div>
  <div class="socials abs"><span class="s1"></span><span class="s2"></span><span class="s3"></span></div>
  <nav class="main-nav abs">
    <a class="active">Home</a><a>The Institute</a><a>Service Dog Organizations</a><a>Building Trainers</a><a>Research</a><a>Contact</a>
  </nav>
</header>

<section class="hero abs">
  <div class="hero-photo abs photo" role="img" aria-label="Golden retriever service dog in a vest looking up"></div>
  <div class="hero-copy abs" style="left:860px;top:150px">
    <div class="kicker">Coaching for</div>
    <h1>Service Dog<br>Professionals</h1>
    <span class="btn">Get Started</span>
  </div>

  <div class="center-card abs">
    <div class="pre">Brevant Moor Institute for</div>
    <h2>Applied Alert Dog Studies</h2>
    <p>Brevant Moor Institute was founded by Marisa Holloway Ph.D. in response to demand for coaching from dog trainers, medical professionals and service dog programs. Our team has helped hundreds of trainers and service dog programs, both in the US and internationally, expand the type of dogs they train.</p>
    <span class="btn">Read More</span>
  </div>

  <div class="founder-card abs">
    <h3>Marisa Holloway</h3>
    <div class="avatar" role="img" aria-label="Portrait of the founder"></div>
    <blockquote>“Training service dogs is a rewarding career for those who care about dogs and people. It requires empathy, dedication, patience, and a good base of knowledge in dog behavior and psychology.”</blockquote>
    <div class="sig">Marisa Holloway Ph.D.</div>
    <div class="role">Founder</div>
  </div>
</section>

<h2 class="courses-title abs">Dog Training Courses</h2>

<article class="course abs" style="left:130px;top:1032px">
  <div class="photo" role="img" aria-label="Trainer working with a dog in a store"></div>
  <h4>All you need to train a medical assistance dog</h4>
  <p>Learn everything you need to become a professional service dog trainer and specialize in medical alert dogs. This is an in-depth, comprehensive, hands-on curriculum that will give you all the information.</p>
  <span class="btn">Read More</span>
</article>
<article class="course abs" style="left:450px;top:1032px">
  <div class="photo" role="img" aria-label="Row of dog kennels at a shelter"></div>
  <h4>Service dog candidate selection</h4>
  <p>This course covers everything about dogs. You will learn to use our temperament testing protocols, our selection and genetic tests on temperament to learn how to select the right dog to train as service dogs.</p>
  <span class="btn">Read More</span>
</article>
<article class="course abs" style="left:770px;top:1032px">
  <div class="photo" role="img" aria-label="Group of trainers with dogs in a classroom"></div>
  <h4>Service Dog Training and Assessments</h4>
  <p>A solid service dog program requires dependable tracking, and testing protocols for the dogs in training. This is about the basics for all service dogs, no matter the disability they will help.</p>
  <span class="btn">Read More</span>
</article>

<article class="course abs" style="left:130px;top:1412px">
  <div class="photo" role="img" aria-label="Service dog performing a task at home"></div>
  <h4>Medical Assistance Dog Tasks</h4>
  <p>This course will cover everything you need to learn about medical assistance dog training and will give you practical hands-on training experience. While disabilities can be related.</p>
  <span class="btn">Read More</span>
</article>
<article class="course abs" style="left:450px;top:1412px">
  <div class="photo" role="img" aria-label="Dog and handler walking through an airport"></div>
  <h4>Public Access</h4>
  <p>Service dogs must work in public places. This is the hardest part of the training as many dogs struggle with the level of distractions and stimuli present in the environment.</p>
  <span class="btn">Read More</span>
</article>
<article class="course abs" style="left:770px;top:1412px">
  <div class="photo" role="img" aria-label="Service dog beside a client"></div>
  <h4>The Clients</h4>
  <p>We train service dogs so they can help a person with a disability. This course focuses on the human side, with the challenges and its successes! How to select service dog clients.</p>
  <span class="btn">Read More</span>
</article>

<div class="band abs"></div>
<div class="big-word abs" style="left:190px">ASSISTANCE</div>
<div class="big-word abs" style="left:690px">CANINES</div>
<div class="dog-art abs" role="img" aria-label="Illustration of a sitting labrador puppy"></div>

<svg class="arrow abs" style="left:100px" viewBox="0 0 30 30" aria-hidden="true"><path d="M19 7 11 15l8 8" fill="none" stroke="#555" stroke-width="2"/></svg>
<svg class="arrow abs" style="left:1070px" viewBox="0 0 30 30" aria-hidden="true"><path d="M11 7l8 8-8 8" fill="none" stroke="#555" stroke-width="2"/></svg>

<article class="slide abs" style="left:150px;top:2092px">
  <div class="photo" role="img" aria-label="Dog resting on a tiled floor in an office"></div>
  <h4>Organization/Program Consulting</h4>
  <p>Helping organizations get started, improve their training programs, and add services.</p>
  <span class="btn">Read More</span>
</article>
<article class="slide abs" style="left:455px;top:2252px">
  <div class="photo" role="img" aria-label="Trainer coaching with a dog outdoors in a field"></div>
  <h4>Professional coaching teaching the dog trainers</h4>
  <p>Helping dog trainers improve their skills and learn about service dog training and medical alert dog training.</p>
  <span class="btn">Read More</span>
</article>
<article class="slide abs" style="left:775px;top:2092px">
  <div class="photo" role="img" aria-label="Researchers with dogs in a training hall"></div>
  <h4>Collaborating in Research Projects</h4>
  <p>Collaborating in research studies in the field of Medical Assistance Dogs.</p>
  <span class="btn">Read More</span>
</article>

<div class="book abs" role="img" aria-label="Book cover: Paws on the Pavement, with a dog on the cover"></div>
<div class="book-copy abs">
  <div class="pre">New book from</div>
  <h2>Marisa Holloway Ph.D.!</h2>
  <p>Paws on the Pavement: A Field Guide for Working Teams in Public Spaces</p>
  <span class="btn dark">Learn More</span>
</div>

<section class="ahead abs" role="img" aria-label="Dark blue background with a dog and handler">
  <h2>Staying Ahead</h2>
  <p>Science-based and ethical training methods for the modern service dog trainer</p>
  <span class="btn">Get Started</span>
</section>

<footer class="site-footer abs">
  <div class="fcol abs" style="left:140px">
    <h5>Sitemap</h5>
    Home<br>The Institute<br>Service Organizations<br>Building Trainers<br>Research<br>Contact
  </div>
  <div class="fcol abs" style="left:330px">
    <h5>Contact Us</h5>
    <span class="ico"></span>42 Alder Ridge Way, Suite 7<br><span class="ico" style="visibility:hidden"></span>Fernwood<br>
    <span class="ico"></span>+1 (555) 014-2286<br>
    <span class="ico"></span>hello@brevantmoor.example
  </div>
  <div class="fcol abs" style="left:560px">
    <h5>Organization</h5>
    Consulting<br>Courses<br>International Coaching
  </div>
  <div class="fcol abs" style="left:760px">
    <h5>Get In Touch</h5>
    <div class="field"></div>
    <div class="field"></div>
    <span class="btn">Send Message</span>
  </div>
  <div class="fcol abs" style="left:960px">
    <h5>Follow Us</h5>
    <div class="fsoc"><span class="s1"></span>Community</div>
    <div class="fsoc"><span class="s2"></span>Updates</div>
    <div class="fsoc"><span class="s3"></span>Videos</div>
  </div>
  <div class="copyright abs">Copyright © 2024 Brevant Moor Institute · Alert Dog Coaching. All rights reserved.</div>
</footer>

</body>
</html>
```